3rd Annual Maple & Clover Fundraiser

This is our 3rd Annual Maple & Clover Dog Wash Extravagana to support Circle of Harlow Ridge Pet Center. Please see the attached flyer for the 2nd Annual. We loved this flyer! Please revamp with our logo attached and the new content provided. Let's keep to the same colors as the 2nd Annual flyer-no change. Date: Saturday April 25th 2020 10A-1PM. Rain Date: May 2nd. Same address as 2nd Annual.

Other font styles liked:
• See 2nd Annual Flyer

Colors
add136
e34297
6b449b

Requirements
Must have
• See attached 2nd annual flyer including colors
Nice to have

```html
<!DOCTYPE html>
<html lang="en">
<head>
<meta charset="utf-8">
<title>Maple &amp; Clover – Doggie Wash Extravaganza</title>
<link href="https://fonts.googleapis.com/css2?family=Montserrat:wght@400;500;600;700;800&family=Righteous&display=swap" rel="stylesheet">
<style>
:root{
  --green:#add136;
  --pink:#e34297;
  --purple:#6b449b;
  --purple-soft:#8a66b4;
  --ink:#1d1d1f;
  --paper:#ffffff;
}
*{margin:0;padding:0;box-sizing:border-box}
html,body{width:703px;height:1200px;overflow:hidden;background:var(--paper)}
body{font-family:"Montserrat",sans-serif;color:var(--ink)}
.flyer{position:relative;width:703px;height:1200px;overflow:hidden;background:var(--paper)}
.abs{position:absolute}
.hero{left:0;top:0}
.photo-circle{border-radius:50%;border:7px solid var(--green)}
.photo-circle.pink{border-color:var(--pink)}
.circle-dogs{left:540px;top:224px;width:132px;height:132px;background:radial-gradient(circle at 50% 40%,#9bb8c9,#7c8a5a 70%,#b9865a)}
.circle-kiss{left:482px;top:347px;width:160px;height:160px;background:radial-gradient(circle at 55% 55%,#c98a55,#6f4a3b 60%,#d8c3b6)}
.circle-mascot{left:400px;top:453px;width:114px;height:114px;background:radial-gradient(circle at 45% 50%,#8b5a2e,#7f9c5a 70%,#c8d3d8)}
.annual{left:44px;top:470px;font-weight:700;font-size:27px;color:var(--pink);letter-spacing:-.3px}
.event-name{left:44px;top:516px;font-weight:800;font-size:42px;color:var(--purple);letter-spacing:-1px;line-height:1}
.tagline{left:46px;top:572px;font-weight:600;font-size:12px;color:var(--pink);letter-spacing:7px}
.support{left:528px;top:547px;font-weight:600;font-size:18px;color:var(--pink)}
.partner{left:514px;top:582px;width:170px;text-align:center}
.partner-name{font-weight:800;font-size:19px;line-height:1.15;color:var(--ink)}
.partner-line{margin-top:8px;font-size:9.5px;font-weight:500;line-height:1.35}
.headline{left:42px;top:620px;font-family:"Righteous",sans-serif;font-size:25px;color:var(--purple);letter-spacing:1.4px}
.pill{left:37px;top:657px;width:396px;height:38px;border-radius:19px;background:var(--pink);color:#fff;font-weight:700;font-size:19.5px;text-align:center;line-height:38px;letter-spacing:.3px}
.when{left:72px;top:744px;font-weight:700;font-size:17.5px;line-height:1.25}
.when-row{display:flex;gap:8px;align-items:flex-start}
.when-row+.when-row{margin-top:16px}
.divider-v{left:357px;top:744px;width:1px;height:72px;background:#c9c9c9}
.where{left:430px;top:744px;display:flex;gap:7px;font-weight:700;font-size:17.5px;line-height:1.25}
.perks{left:36px;top:857px;width:634px;height:124px;border-radius:32px;background:var(--purple-soft)}
.perk-list{position:absolute;top:18px;list-style:none;color:#fff;font-size:14px;font-weight:500;line-height:21px}
.perk-list li{display:flex;align-items:center;gap:7px}
.perk-a{left:34px}.perk-b{left:296px}.perk-c{left:500px}
.perk-sep{position:absolute;top:18px;width:1px;height:60px;background:rgba(255,255,255,.6)}
.donate{left:68px;top:946px;width:565px;height:46px;border-radius:23px;background:var(--green);overflow:hidden;display:flex;align-items:center;color:#fff;font-size:13.5px}
.donate-url{padding-left:28px;flex:1}
.donate-url b{font-weight:700}
.donate-cta{width:148px;height:100%;background:var(--pink);font-weight:700;display:flex;align-items:center;justify-content:center;clip-path:polygon(8% 0,100% 0,100% 100%,0 100%)}
.note{left:60px;top:1014px;width:500px;font-size:14.5px;line-height:1.25;font-weight:500}
.rule{left:60px;top:1064px;width:530px;height:1px;background:#cfcfcf}
.dog-photo{left:606px;top:980px;width:97px;height:220px;background:linear-gradient(160deg,#ffffff 0%,#c79a62 35%,#6a4526 70%,#3a2a1e 100%);border-top-left-radius:90px 140px}
.contact{top:1094px;font-size:11.5px;line-height:16.5px}
.contact strong{font-weight:700}
.contact-a{left:134px}.contact-b{left:406px}
.mini-org{top:1100px;font-weight:800;font-size:11px;line-height:1.2;text-align:center;color:var(--ink)}
.mini-org-a{left:44px;width:82px}
.mini-org-b{left:292px;width:106px;color:var(--purple)}
.divider-foot{left:280px;top:1096px;width:1px;height:58px;background:#bdbdbd}
</style>
</head>
<body>
<main class="flyer">
  <svg class="abs hero" width="703" height="430" viewBox="0 0 703 430">
    <defs>
      <linearGradient id="photoTone" x1="0" y1="0" x2="0" y2="1">
        <stop offset="0" stop-color="#3f6a2e"/>
        <stop offset=".45" stop-color="#8aa6b8"/>
        <stop offset=".75" stop-color="#c46a3e"/>
        <stop offset="1" stop-color="#3c5d9c"/>
      </linearGradient>
    </defs>
    <path role="img" aria-label="Group photo of volunteers in event t-shirts with a dog mascot outdoors" fill="url(#photoTone)" d="M0 0H703V330C520 360 260 385 0 352Z"/>
    <path fill="var(--purple-soft)" d="M0 352C260 385 520 360 703 330V346C520 385 300 420 0 412Z"/>
  </svg>

  <div class="abs photo-circle circle-dogs" role="img" aria-label="Photo of a dog being washed"></div>
  <div class="abs photo-circle pink circle-kiss" role="img" aria-label="Photo of a girl hugging a small dog"></div>
  <div class="abs photo-circle circle-mascot" role="img" aria-label="Photo of the dog mascot holding a free doggie wash sign"></div>

  <div class="abs annual">Third Annual</div>
  <div class="abs event-name">Maple &amp; Clover</div>
  <div class="abs tagline">DO A LITTLE. CHANGE A LOT.</div>

  <div class="abs support">In support of</div>
  <div class="abs partner">
    <div class="partner-name">Circle of Harlow Ridge Pet Center</div>
    <div class="partner-line">Adopt a forever friend…<br>You will be their hero</div>
  </div>

  <div class="abs headline">DOGGIE WASH EXTRAVAGANZA</div>
  <div class="abs pill">A FAMILY FUN EVENT FOR ALL AGES</div>

  <div class="abs when">
    <div class="when-row">
      <svg width="20" height="20" viewBox="0 0 20 20"><rect x="2" y="4" width="16" height="14" rx="2" fill="none" stroke="#222" stroke-width="1.6"/><line x1="2" y1="8" x2="18" y2="8" stroke="#222" stroke-width="1.6"/><line x1="6" y1="2" x2="6" y2="5" stroke="#222" stroke-width="1.6"/><line x1="14" y1="2" x2="14" y2="5" stroke="#222" stroke-width="1.6"/><g fill="#222"><rect x="5" y="10.5" width="2" height="2"/><rect x="9" y="10.5" width="2" height="2"/><rect x="13" y="10.5" width="2" height="2"/><rect x="5" y="14" width="2" height="2"/><rect x="9" y="14" width="2" height="2"/></g></svg>
      <span>Saturday April 25th 2020<br>Rain Date May 2nd</span>
    </div>
    <div class="when-row">
      <svg width="20" height="20" viewBox="0 0 20 20"><circle cx="10" cy="10" r="8.2" fill="none" stroke="#222" stroke-width="1.8"/><path d="M10 5V10.5L13 13" fill="none" stroke="#222" stroke-width="1.8"/></svg>
      <span>10am - 1pm</span>
    </div>
  </div>
  <div class="abs divider-v"></div>
  <div class="abs where">
    <svg width="14" height="22" viewBox="0 0 14 22"><path d="M7 1C3.7 1 1 3.6 1 6.8 1 11 7 19 7 19S13 11 13 6.8C13 3.6 10.3 1 7 1Z" fill="none" stroke="#222" stroke-width="1.8"/><circle cx="7" cy="7" r="2.2" fill="#222"/></svg>
    <span>Linden Realty, 318<br>Harbor Walk Ave. Ponte<br>Vedra FL32081<br>Seabrook Town Center</span>
  </div>

  <section class="abs perks">
    <ul class="perk-list perk-a">
      <li><svg width="12" height="12" viewBox="0 0 12 12"><rect x="1" y="1" width="10" height="10" rx="2" fill="none" stroke="var(--green)" stroke-width="1.3"/><path d="M3 6L5.2 8.2L10.5 2" fill="none" stroke="var(--green)" stroke-width="1.6"/></svg>Free Doggie Wash</li>
      <li><svg width="12" height="12" viewBox="0 0 12 12"><rect x="1" y="1" width="10" height="10" rx="2" fill="none" stroke="var(--green)" stroke-width="1.3"/><path d="M3 6L5.2 8.2L10.5 2" fill="none" stroke="var(--green)" stroke-width="1.6"/></svg>Food &amp; Beverages</li>
      <li><svg width="12" height="12" viewBox="0 0 12 12"><rect x="1" y="1" width="10" height="10" rx="2" fill="none" stroke="var(--green)" stroke-width="1.3"/><path d="M3 6L5.2 8.2L10.5 2" fill="none" stroke="var(--green)" stroke-width="1.6"/></svg>Vendors (Free give-a-way)</li>
    </ul>
    <span class="perk-sep" style="left:276px"></span>
    <ul class="perk-list perk-b">
      <li><svg width="12" height="12" viewBox="0 0 12 12"><rect x="1" y="1" width="10" height="10" rx="2" fill="none" stroke="var(--green)" stroke-width="1.3"/><path d="M3 6L5.2 8.2L10.5 2" fill="none" stroke="var(--green)" stroke-width="1.6"/></svg>Raffle drawings</li>
      <li><svg width="12" height="12" viewBox="0 0 12 12"><rect x="1" y="1" width="10" height="10" rx="2" fill="none" stroke="var(--green)" stroke-width="1.3"/><path d="M3 6L5.2 8.2L10.5 2" fill="none" stroke="var(--green)" stroke-width="1.6"/></svg>Grand Prize</li>
      <li><svg width="12" height="12" viewBox="0 0 12 12"><rect x="1" y="1" width="10" height="10" rx="2" fill="none" stroke="var(--green)" stroke-width="1.3"/><path d="M3 6L5.2 8.2L10.5 2" fill="none" stroke="var(--green)" stroke-width="1.6"/></svg>Donations Welcome</li>
    </ul>
    <span class="perk-sep" style="left:480px"></span>
    <ul class="perk-list perk-c">
      <li style="align-items:flex-start"><svg width="12" height="12" viewBox="0 0 12 12" style="margin-top:3px"><rect x="1" y="1" width="10" height="10" rx="2" fill="none" stroke="var(--green)" stroke-width="1.3"/><path d="M3 6L5.2 8.2L10.5 2" fill="none" stroke="var(--green)" stroke-width="1.6"/></svg><span>Adoptions by<br>CHRPC</span></li>
    </ul>
  </section>

  <div class="abs donate">
    <span class="donate-url">TO MAKE A DONATION:&nbsp; <b>https://www.chrpc.org/donate/</b></span>
    <span class="donate-cta">CLICK: DONATE</span>
  </div>

  <p class="abs note">All Domestic breeds from puppies to senior invited. Please be sure Furry Fido is tolerant of other dogs, crowds and bathing</p>
  <div class="abs rule"></div>

  <div class="abs dog-photo" role="img" aria-label="Photo of a German shepherd being brushed"></div>

  <div class="abs mini-org mini-org-a">Circle of Harlow Ridge Pet Center</div>
  <div class="abs contact contact-a"><strong>DANA WHITLOCK</strong><br>CHRPC<br>904.555.0173<br>dana-whitlock@mailbay.net</div>
  <div class="abs divider-foot"></div>
  <div class="abs mini-org mini-org-b">Renee Castell<br>Linden Realty</div>
  <div class="abs contact contact-b"><strong>RENEE CASTELL</strong><br>Linden Realty Group<br>770.555.0147<br>renee@lindenrealtygroup.com</div>
</main>
</body>
</html>
```